Fernbrook Pet Showcase Ticket Card Design

We’re looking to create a complimentary “ticket” card for Fernbrook Pet Showcase that can be handed out physically. We host an event for cat lovers. The card should feel special and collectible. Size will be a standard business card (3.5" x 2") Orientation is open to designer recommendation. This ticket will be used as a complimentary entry pass for select guests, partners, & giveaways. Key elements to Include are the Fernbrook Pet Showcase logo (provided), the words “Complimentary Ticket” or similar wording (open to creative phrasing and cat puns) A blank space for the Event date (to be written in) & Ticket number (to be written in) . Event Name is always "Fernbrook Pet Bazaar & Rehoming Day". We want the ticket to feel clean & modern but slightly playful with a cat-inspired touch (think clever, not kitschy). Could include a subtle cat motif or texture (e.g., whisker lines, paw detail, soft patterning) Open to unique layout ideas that still leave clear writing space. Avoid overcrowding of elements. Ticket should also have fine print "This ticket is not redeemable for cash and cannot be combined with any other offers or discounts, can only be used for the date indicated"

Target Market(s)

Women

Industry/Entity Type

pets

Colors
6B429C
8869AF
B7A5CE
E3DAEB
F3F0F8

Requirements
Must have
• Fernbrook Pet Showcase Logo & words around complimentary ticket as well as the fine print
Nice to have
• cat-inspired touch (think clever, not kitschy). Could include a subtle cat motif or texture (e.g., whisker lines, paw detail, soft patterning)
Should not have
• should not look cartoony

```html
<!DOCTYPE html>
<html lang="en">
<head>
<meta charset="UTF-8">
<title>Fernbrook Pet Showcase – Complimentary Ticket</title>
<link href="https://fonts.googleapis.com/css2?family=Montserrat:wght@300;400;500;600;700&display=swap" rel="stylesheet">
<style>
  :root {
    --band: #9886B6;
    --band-deep: #8869AF;
    --card: #DCD2E8;
    --card-light: #E3DAEB;
    --panel: #F7F5FA;
    --ink: #3E2D55;
    --ink-soft: #4A3D5C;
    --subtitle: #F3F0F8;
    --white: #FFFFFF;
  }
  * { margin: 0; padding: 0; box-sizing: border-box; }
  html, body { width: 1200px; height: 800px; overflow: hidden; background: var(--card); }
  .ticket {
    position: relative;
    width: 1200px;
    height: 800px;
    background: var(--card);
    font-family: "Montserrat", sans-serif;
    color: var(--ink);
    overflow: hidden;
  }
  .ticket__band {
    position: absolute;
    left: 0; top: 0;
    width: 1200px; height: 318px;
    background: linear-gradient(180deg, #9C8AB9 0%, var(--band) 100%);
  }
  .brand-name {
    position: absolute;
    left: 0; top: 78px;
    width: 1200px;
    text-align: center;
    color: var(--white);
    font-weight: 500;
    font-size: 58px;
    line-height: 66px;
    letter-spacing: 1px;
    text-transform: uppercase;
  }
  .ticket__title {
    position: absolute;
    left: 0; top: 368px;
    width: 1200px;
    text-align: center;
    font-weight: 600;
    font-size: 62px;
    letter-spacing: 2px;
    color: var(--ink);
  }
  .ticket__event {
    position: absolute;
    left: 0; top: 456px;
    width: 1200px;
    text-align: center;
    font-weight: 500;
    font-size: 30px;
    letter-spacing: 1.5px;
    color: var(--subtitle);
    text-transform: uppercase;
  }
  .entry-panel {
    position: absolute;
    left: 63px; top: 522px;
    width: 1075px; height: 147px;
    background: var(--panel);
    border-radius: 18px;
  }
  .entry-field {
    position: absolute;
    display: flex;
    align-items: baseline;
    font-weight: 600;
    font-size: 33px;
    letter-spacing: 1px;
    color: var(--ink);
  }
  .entry-field__line {
    display: inline-block;
    height: 2px;
    margin-left: 14px;
    border-bottom: 2px dotted var(--ink-soft);
  }
  .entry-field--date { left: 45px; top: 40px; }
  .entry-field--date .entry-field__line { width: 395px; }
  .entry-field--number { left: 600px; top: 40px; }
  .entry-field--number .entry-field__line { width: 195px; }
  .entry-panel__extra-line {
    position: absolute;
    left: 45px; top: 113px;
    width: 988px;
    border-bottom: 2px dotted var(--ink-soft);
  }
  .fine-print {
    position: absolute;
    left: 0; top: 688px;
    width: 1200px;
    text-align: center;
    font-weight: 400;
    font-size: 23px;
    line-height: 33px;
    color: var(--ink-soft);
  }
  .paw {
    position: absolute;
    top: 716px;
    width: 62px; height: 62px;
    border-radius: 50%;
    background: var(--band);
    opacity: 0.8;
  }
  .paw--left { left: 34px; }
  .paw--right { right: 34px; }
  .ticket__wave { position: absolute; left: 0; bottom: 0; }
</style>
</head>
<body>
  <main class="ticket">
    <div class="ticket__band" role="img" aria-label="Soft line-art pattern of cat faces, whiskers and looping tails in white on lavender"></div>
    <h1 class="brand-name">Fernbrook<br>Pet<br>Showcase</h1>

    <h2 class="ticket__title">COMPLIMENTARY TICKET</h2>
    <p class="ticket__event">Fernbrook Pet Bazaar &amp; Rehoming Day</p>

    <section class="entry-panel">
      <div class="entry-field entry-field--date">DATE:<span class="entry-field__line"></span></div>
      <div class="entry-field entry-field--number">TICKET NO:<span class="entry-field__line"></span></div>
      <div class="entry-panel__extra-line"></div>
    </section>

    <p class="fine-print">This ticket is not redeemable for cash and cannot be combined with any<br>other offers or discounts, can only be used for the date indicated.</p>

    <div class="paw paw--left" role="img" aria-label="Paw print ornament"></div>
    <div class="paw paw--right" role="img" aria-label="Paw print ornament"></div>

    <svg class="ticket__wave" width="1200" height="40" viewBox="0 0 1200 40" aria-hidden="true">
      <path d="M0 30 C 250 6, 450 6, 700 18 S 1050 22, 1200 14 L1200 40 L0 40 Z" fill="var(--band)"/>
      <path d="M0 30 C 250 6, 450 6, 700 18 S 1050 22, 1200 14" fill="none" stroke="var(--white)" stroke-width="2" opacity="0.8"/>
    </svg>
  </main>
</body>
</html>
```